Skincare ..product is Velmorique revolutionary new skincare product that has created a break thru fo

we need a 5x8 dimension mail piece emphasizing Velmorique Body lotion and Face cream.......this will be sent to potential distributors.....Velmorique is a revolutionary new skin care product designed with an encapsulation process at an FDA lab with emphasis on the proprietary blend QRT.....concentrated hemp extract patent pending that penetrates deeper into the skin....creating a significant anti aging effect on the skin!

Target Market(s)

spas and salons ...women 35-65

Industry/Entity Type

Product

Colors
ffffff
acd037

Requirements
Must have
• picture of the body lotion and the face cream FDA lab approved CBD hemp extract formulation.....amazing results...*. Softest skin balm around or softestskinbalmaround.example.....* Great margins for our distribution partners!....*.Hawaiian vacation for top distributors! WWW.Plumvaleessentia.example
Nice to have
• call 555-318-4720 picture of model on our site.....

```html
<!DOCTYPE html>
<html lang="en">
<head>
<meta charset="utf-8">
<title>Velmorique Distributor Mailer</title>
<link rel="stylesheet" href="https://fonts.googleapis.com/css2?family=Source+Sans+3:wght@400;600;700&display=swap">
<style>
  :root {
    --stage: #5a5a5a;
    --paper: #ffffff;
    --lime: #acd037;
    --lime-shade: #9cbf2c;
    --teal: #15706a;
    --ink-grey: #7d7d7d;
    --ink-dark: #333333;
  }
  html, body {
    margin: 0;
    padding: 0;
    width: 1200px;
    height: 1083px;
    overflow: hidden;
    background: var(--stage);
  }
  .canvas {
    width: 1200px;
    height: 1083px;
    display: flex;
    align-items: center;
    justify-content: center;
  }
  .mailer {
    width: 640px;
    height: 1000px;
    display: block;
    box-shadow: 0 6px 18px rgba(0,0,0,0.35);
    font-family: "Source Sans 3", "Myriad Pro", sans-serif;
  }
  .headline { fill: var(--teal); font-size: 16.5px; font-weight: 400; }
  .subline { fill: var(--paper); font-size: 9.5px; font-weight: 400; }
  .label { fill: var(--paper); font-size: 10px; font-weight: 400; }
  .results { fill: var(--paper); font-size: 28px; font-weight: 600; text-anchor: middle; }
  .margins { fill: var(--teal); font-size: 22px; font-weight: 700; text-anchor: middle; }
  .partners { fill: var(--teal); font-size: 12px; font-weight: 400; text-anchor: middle; }
  .pill-text { fill: var(--paper); font-size: 11.5px; font-weight: 400; text-anchor: middle; }
  .brand-name { fill: var(--ink-grey); font-weight: 400; }
  .brand-tag { fill: var(--ink-grey); font-size: 3.4px; }
  .tagline { fill: var(--teal); font-size: 7px; font-weight: 600; }
  .phone { fill: var(--ink-dark); font-size: 10px; letter-spacing: 2.2px; }
  .site { fill: var(--ink-dark); font-size: 7px; }
</style>
</head>
<body>
<main class="canvas">
  <svg class="mailer" viewBox="0 0 380 594" xmlns="http://www.w3.org/2000/svg">
    <defs>
      <linearGradient id="model-tone" x1="0.3" y1="0" x2="0.7" y2="1">
        <stop offset="0" stop-color="#1e1e1e"/>
        <stop offset="0.22" stop-color="#3a3a3a"/>
        <stop offset="0.45" stop-color="#cfcfcf"/>
        <stop offset="0.75" stop-color="#b4b4b4"/>
        <stop offset="1" stop-color="#8e8e8e"/>
      </linearGradient>
      <linearGradient id="jar-tone" x1="0" y1="0" x2="1" y2="0">
        <stop offset="0" stop-color="#b9bdbf"/>
        <stop offset="0.5" stop-color="#f4f4f4"/>
        <stop offset="1" stop-color="#c4c8ca"/>
      </linearGradient>
      <linearGradient id="bottle-tone" x1="0" y1="0" x2="0" y2="1">
        <stop offset="0" stop-color="#d7d9da"/>
        <stop offset="1" stop-color="#e8d7a8"/>
      </linearGradient>
      <linearGradient id="box-tone" x1="0" y1="0" x2="1" y2="0">
        <stop offset="0" stop-color="#f6f3ea"/>
        <stop offset="1" stop-color="#e3ddcd"/>
      </linearGradient>
      <filter id="soft-glow" x="-20%" y="-40%" width="140%" height="180%">
        <feGaussianBlur in="SourceAlpha" stdDeviation="4"/>
        <feFlood flood-color="#ffffff" flood-opacity="0.7"/>
        <feComposite operator="in" in2="SourceAlpha"/>
        <feMerge><feMergeNode/><feMergeNode in="SourceGraphic"/></feMerge>
      </filter>
    </defs>

    <rect class="paper" width="380" height="594" fill="var(--paper)"/>

    <path class="lime-field" d="M0,0 H380 V383 C280,438 120,446 0,398 Z" fill="var(--lime)"/>

    <path class="model-photo" role="img" aria-label="Black and white photo of a smiling blonde model in a dark hat"
          d="M35,0 H380 V270 C340,288 300,294 260,292 C170,286 85,200 35,0 Z"
          fill="url(#model-tone)"/>
    <path class="photo-edge" d="M35,0 C85,200 170,286 260,292 C300,294 340,288 380,270"
          fill="none" stroke="var(--paper)" stroke-width="4"/>

    <g class="photo-brand">
      <circle cx="300" cy="228" r="13" fill="none" stroke="var(--ink-grey)" stroke-width="1.2"/>
      <text class="brand-name" x="300" y="266" font-size="17" text-anchor="middle">Velmorique</text>
      <text class="brand-tag" x="300" y="273" text-anchor="middle">by Plumvale Essentia</text>
    </g>

    <ellipse class="product-shadow" cx="110" cy="300" rx="90" ry="9" fill="var(--lime-shade)"/>
    <rect class="product-photo jar" role="img" aria-label="Product photo of the silver body lotion jar"
          x="28" y="211" width="94" height="77" rx="8" fill="url(#jar-tone)"/>
    <rect class="product-photo bottle" role="img" aria-label="Product photo of the face cream pump bottle"
          x="124" y="198" width="27" height="92" rx="4" fill="url(#bottle-tone)"/>
    <rect class="product-photo box" role="img" aria-label="Product photo of the face cream box"
          x="153" y="193" width="37" height="93" rx="1" fill="url(#box-tone)"/>

    <text class="label" x="42" y="307">Body Lotion</text>
    <text class="label" x="128" y="307">Face Cream</text>

    <text class="headline" x="42" y="344">Revolutionary Skin</text>
    <text class="headline" x="42" y="365">Care Product</text>
    <text class="subline" x="42" y="387">Fda Lab Approved Cbd Hemp</text>
    <text class="subline" x="42" y="400">Extract Formulation</text>

    <g class="results-callout" filter="url(#soft-glow)">
      <text class="results" x="272" y="371">Amazing</text>
      <text class="results" x="273" y="400">Results</text>
    </g>

    <text class="margins" x="190" y="469">Great Margins</text>
    <text class="partners" x="190" y="484">for our Distribution Partners!</text>
    <rect class="pill" x="91" y="491" width="199" height="24" rx="12" fill="var(--teal)"/>
    <text class="pill-text" x="190.5" y="507">Hawaiian vacation for top distributors</text>

    <g class="footer-brand">
      <circle cx="70" cy="535" r="9" fill="none" stroke="var(--ink-grey)" stroke-width="1"/>
      <text class="brand-name" x="70" y="559" font-size="12.5" text-anchor="middle">Velmorique</text>
      <text class="brand-tag" x="70" y="565" text-anchor="middle">by Plumvale Essentia</text>
    </g>

    <text class="phone" x="253" y="556">555-318-4720</text>
    <text class="site" x="253" y="566">WWW.Plumvaleessentia.example</text>
    <text class="tagline" x="253" y="577">Softest skin balm around</text>
  </svg>
</main>
</body>
</html>
```